Designing a "Yummy Mummy" Style Blog

I am clueless when it comes to technology and web design. I am starting a blog on pregnancy, babies and high society life in London. It's going to be called "Fizzwicks on Marlow", and will aim to be frank, funny and aspire to a certain type of luxury lifestyle.

I would like a well designed, sophisticated looking blog set up for me. I've never had a blog designed for me online before, so i am not entirely sure how it works but ideally i would like the whole "look set up" so i can get the password, add a domain to it and start inputting my text and pictures.

Basically i looked into setting up one myself on pagecraft/scribbleup.example but i realised that with my very basic know how, what i was going to end up with from the "template suggestions" was going to be pretty generic and i really want something unique and special as i am going to try and promote this alongside my writing career.

I would like a relatively non-fussy layout but the "Fizzwicks on Marlow" title i thought could be designed to look like a bit of a logo, with perhaps a cocktail on one end and a dummy/rattle on the other. I want the whole website to look fashionable, stylish and endorse a "yummy mummy lifestyle".

Ideally it would be very easy for me to upload text and pictures to the blog and it would be very visually appealing to look at and easy to read. It will need to have a list of all my blog posts on the side (obviously which are yet to be written, but the capability to have them all in the readers eye-line when they are eventually written!)

I would like to blog to look more like a website than a standard blog. See www.dapperpavement.example or www.vogrenstrand.example for the type of non-standard blog format i like.

Each post is going to be mainly text but then i would like the ability to add photos to each one. I also want the text spread across the page so that it becomes "about the writing"... what i mean is some blogs have lots of little tabs of text you can click on... i want my blog to scroll down so you read it like a story... a bit like www.bumpandbloomdiary.example or www.penvaleposts.example.

Look forward to seeing what you come up with. as an example of my personal style, please see my website www.roseharwick.example which was a clothing brand i designed a few years ago. See that i had an illustration of myself done (in the about section) i like the idea of some little drawings or something unique to make it original. Many thanks for your work in advance.

Please note, i have only made this work "refundable" because i havent done a web design style job post like this before and obviously have no idea whether this is something that would work (have someone design it online for me" BUT i fully intend to buy a design off here and am very serious about doing so so please know that if your design fits what i am looking for i am definitely buying it, this is a genuine committed request!

Many thanks
Updates

Reason: I am extending the deadline as i have just decided to Guarantee the prize money for the project. My email address is rose@roseharwick.example if you would like to email me any ideas/designs for the blog. Please know that i would like the actual blog set up for me on either pagecraft or scribbleup.example site under FIZZWICKS ON MARLOW (my new blog name). Obviously i will be buying the domain name for this but whoever comes up with the best design i will go onto whichever blog site you recommend, add register the FIZZWICKS ON MARLOW BLOG and then you can do all the design for me. Then you will be guaranteed payment on this site. So just know - whoever describes and shows me through logos, fonts and description the best design for my blog will be the one to do it! And i definitely will be choosing someone! Hope my main description give you enough to work out what kind of a style i want. Very modern, femine, fresh fun and clear but not TACKY.. no gaudy colours or pictures.. i want it to look like a glossy magazine column. THANKS x

Target Market(s)

Target market are trendy london girls and new mothers and mothers-to-be. It should appeal to feminine stylish, educated women.

Industry/Entity Type

Clothing

Requirements
Must have
• It must be set up as a blog on an easy to naviagate blog site that i can have easy access to update with my text and pictures using a password and username. It should also be able to have a domain added to it so i can buy www.inkspillsonmarlow.example if i so wish in the future.

INK SPILLS ON MARLOW the title should be designed to look like a logo and be bold and stand out.

The Font needs to be clear yet stylish. I do not want it to be an "all uppercase" font. I am a writer, so i need the ability to use lowercase and uppercase lettering !

Please make it look very clean and clear cut so the reader knows exactly what shes looking at. Some blogs just look too messy, you dont know what you are meant to be reading.

I want the blog to make it clear what the latest blog post is and have that at the top then have all the other blog posts in an archive style list to the left or right of the page. Please make the font clear enough to read but not too huge.

I am sure this goes without saying, but Please note this blog MUST be completely suitable for the UK. I would like it on a UK blog site, or one that is completely worldwide and works for the UK. (ie if this blog is successful i want to make sure i can promote it/advertise on it with uk brands etc)

```html
<!DOCTYPE html>
<html lang="en">
<head>
<meta charset="utf-8">
<title>Fizzwicks on Marlow</title>
<link href="https://fonts.googleapis.com/css2?family=Arimo:wght@400;700&display=swap" rel="stylesheet">
<style>
:root{
  --page-bg:#3a3740;
  --header-top:#4a4756;
  --header-bottom:#35323d;
  --logo-gold:#c9a55a;
  --nav-bg:#d9d9d9;
  --nav-line:#b9b9b9;
  --content-bg:#fbfbfb;
  --title-bar:#f1f1f1;
  --title-text:#6a6a6a;
  --body-text:#333333;
  --meta-text:#666666;
  --panel-bg:#ececec;
  --heading-light:#f4f4f4;
  --heading-dark:#d6d6d6;
  --link:#666666;
}
*{margin:0;padding:0;box-sizing:border-box}
html,body{width:1200px;height:1064px;overflow:hidden}
body{background:var(--page-bg);font-family:"Arimo",Arial,sans-serif;color:var(--body-text);position:relative}
.site{position:absolute;left:132px;top:0;width:936px;height:1064px;background:var(--content-bg)}
.site-header{position:absolute;left:0;top:0;width:936px;height:164px;background:linear-gradient(180deg,var(--header-top),var(--header-bottom))}
.logo-glass{position:absolute;left:2px;top:20px;width:80px;height:120px;border-radius:8px;background:linear-gradient(160deg,#d23a4a,#a5a0a8)}
.logo-soother{position:absolute;left:636px;top:30px;width:92px;height:112px;border-radius:40px;background:linear-gradient(160deg,#e2c25a,#4a6fa8)}
.logo-name{position:absolute;left:88px;top:78px;width:540px;font-weight:700;font-size:41px;letter-spacing:-0.5px;color:var(--logo-gold);white-space:nowrap;line-height:50px}
.main-nav{position:absolute;left:0;top:164px;width:936px;height:45px;background:var(--nav-bg);border-bottom:1px solid var(--nav-line)}
.main-nav a{position:absolute;top:15px;font-size:13px;color:#333;text-decoration:none}
.post-title{position:absolute;left:35px;width:608px;height:31px;background:var(--title-bar);font-size:20.5px;font-weight:700;color:var(--title-text);padding:5px 2px;line-height:22px}
.post-photo{position:absolute;left:35px;width:281px;height:281px}
.post-text{position:absolute;left:329px;width:314px;font-size:13.4px;line-height:15px;color:var(--body-text)}
.post-text .more{color:var(--meta-text)}
.post-meta{position:absolute;left:36px;font-size:13px;color:var(--meta-text)}
.post-meta svg{vertical-align:-1px;margin:0 4px 0 4px}
.sidebar-panel{position:absolute;left:673px;width:249px;background:var(--panel-bg)}
.search-box{position:absolute;left:14px;top:15px;width:220px;height:21px;background:#fff;border:1px solid #999;border-top-color:#666}
.search-box svg{position:absolute;right:4px;top:3px}
.widget-title{position:absolute;left:10px;top:10px;width:229px;height:37px;background:linear-gradient(180deg,var(--heading-light),var(--heading-dark));font-size:14px;font-weight:700;color:#111;padding:11px 0 0 23px}
.widget-title::before{content:"";position:absolute;left:5px;top:12px;width:10px;height:10px;border:2px solid #666;border-radius:50%;background:#ddd}
.widget-list{position:absolute;left:25px;top:57px;width:215px;list-style:none;font-size:12.5px;line-height:16.5px;color:#555}
.widget-list li{position:relative;padding-left:11px;margin-bottom:4px}
.widget-list li::before{content:"»";position:absolute;left:0;top:0;font-size:10px;color:#666}
.widget-list a{color:var(--link);text-decoration:underline}
</style>
</head>
<body>
<div class="site">
  <header class="site-header" role="img" aria-label="Dark lilac header with soft bokeh lights">
    <div class="logo-glass" role="img" aria-label="Illustration of a cocktail glass with a strawberry"></div>
    <div class="logo-name">FIZZWICKS ON MARLOW</div>
    <div class="logo-soother" role="img" aria-label="Illustration of a gold and blue baby soother"></div>
  </header>

  <nav class="main-nav">
    <a href="#" style="left:38px">Home</a>
    <a href="#" style="left:139px">About Me</a>
    <a href="#" style="left:263px">Contact</a>
  </nav>

  <article class="post">
    <h2 class="post-title" style="top:232px">Sample Post</h2>
    <div class="post-photo" style="top:287px;background:linear-gradient(135deg,#e8c68a,#d9a06a 50%,#6aa6c8)" role="img" aria-label="Photo of two smiling friends out shopping"></div>
    <p class="post-text" style="top:274px">&nbsp;Lorem ipsum dolor sit amet, alia iudico decore ea pro, ut utinam pertinacia temporibus qui. Habeo quaestio gloriatur ne ius. Ne graeco gubergren torquatos sit, qui cu tollit euripidis conceptam. Nisl antiopam petentium cu vix, ex nullam luptatum suavitate nam.An sit nisl errem, sed eu etiam viris debitis. No elitr convenire moderatius quo. Mea molestie definiebas in. Eros solum electram ut mel, te partem iisque gloriatur eam, ei veniam hendrerit repudiandae has. Detracto invenire est cu.An vim minim timeam alterum. Laudem insolens senserit per ne, eum esse legendos ad. Sit et oratio laudem, vis te diceret blandit liberavisse. Pro ut salutandi quaerendum, his no odio nominavi. &nbsp; <span class="more">Continue reading →</span></p>
    <p class="post-meta" style="top:583px">Posted in Uncategorized | <svg width="14" height="12" viewBox="0 0 14 12"><path d="M1 1h12v7H6l-3 3V8H1z" fill="#ccc" stroke="#888"/></svg> Leave a comment</p>
  </article>

  <article class="post">
    <h2 class="post-title" style="top:658px">Lorem ipsum dolor</h2>
    <div class="post-photo" style="top:713px;background:linear-gradient(160deg,#2a1a14,#c0583a 45%,#7a5a8a)" role="img" aria-label="Photo of a laughing baby in a knitted hat and stripy scarf"></div>
    <p class="post-text" style="top:700px">Lorem ipsum dolor sit amet, alia iudico decore ea pro, ut utinam pertinacia temporibus qui. Habeo quaestio gloriatur ne ius. Ne graeco gubergren torquatos sit, qui cu tollit euripidis conceptam. Nisl antiopam petentium cu vix, ex nullam luptatum suavitate nam.An sit nisl errem, sed eu etiam viris debitis. No elitr convenire moderatius quo. Mea molestie definiebas in. Eros solum electram ut mel, te partem iisque gloriatur eam, ei veniam hendrerit repudiandae has. Detracto invenire est cu.An vim minim timeam alterum. Laudem insolens senserit per ne, eum esse legendos ad. Sit et oratio laudem, vis te diceret blandit liberavisse. Pro ut salutandi quaerendum, his no odio nominavi. In nam esse labore, <span class="more">Continue reading →</span></p>
    <p class="post-meta" style="top:1009px">Posted in Uncategorized | <svg width="14" height="12" viewBox="0 0 14 12"><path d="M1 1h12v7H6l-3 3V8H1z" fill="#ccc" stroke="#888"/></svg> Leave a comment</p>
  </article>

  <aside class="sidebar">
    <section class="sidebar-panel" style="top:211px;height:56px">
      <div class="search-box"><svg width="13" height="13" viewBox="0 0 13 13"><circle cx="5" cy="5" r="4" fill="none" stroke="#999" stroke-width="1.3"/><path d="M8 8l4 4" stroke="#999" stroke-width="1.5"/></svg></div>
    </section>
    <section class="sidebar-panel" style="top:273px;height:166px">
      <h3 class="widget-title">Latest Posts</h3>
      <ul class="widget-list">
        <li><a href="#">Sample Post</a></li>
        <li><a href="#">Lorem ipsum dolor</a></li>
        <li><a href="#">How to: Velmonte's ethereal half-up hairstyle</a></li>
        <li><a href="#">Baby Lorem ipsum dolor</a></li>
      </ul>
    </section>
    <section class="sidebar-panel" style="top:444px;height:126px">
      <h3 class="widget-title">Recent Comments</h3>
      <ul class="widget-list">
        <li>admin on <a href="#">About Me</a></li>
        <li>Mr Pagecraft on <a href="#">Baby Lorem ipsum dolor</a></li>
      </ul>
    </section>
    <section class="sidebar-panel" style="top:576px;height:89px">
      <h3 class="widget-title">Archives</h3>
      <ul class="widget-list"><li><a href="#">November 2012</a></li></ul>
    </section>
    <section class="sidebar-panel" style="top:670px;height:89px">
      <h3 class="widget-title">Categories</h3>
      <ul class="widget-list"><li><a href="#">Uncategorized</a></li></ul>
    </section>
  </aside>
</div>
</body>
</html>
```